Community Management Cooperative Needs a Postcard Design

This will be the first postcard in a 3 part series to be sent to 2,500 management companies in the United States. Neighborhood & Residents Purchasing Alliance helps management companies and communities save money by combining their buying power to drive down costs on everyday business needs. Their membership in the cooperative also connects with other like minded companies in the industry allowing them to share ideas and best practices with one another so that they may improve their business practices. Visit http://joinvelarta.com for more information about the company.

The purpose of this postcard is to get potential members to visit our website to find out more about the cooperative and hopefully apply to become a member. This postcard should convey a message along the lines of "we want you" or "joining forces". I would like to use bright colors and make it eye catching. Can be things along the lines of (but not limited to) super heroes coming together or a patriotic theme, etc. Postcard does not have to be limited to company color palette but provided for reference.
Updates

Target Market(s)

Independent community management companies in the United States, mostly around metropolitan areas. CEO's of companies are usually male and older, 50+

Industry/Entity Type

Community

Requirements
Must have
• Must incorporate our name, logo, and website into the design with a call to action to visit the website.
• http://joinvelarta.com

```html
<!DOCTYPE html>
<html lang="en">
<head>
<meta charset="utf-8">
<title>Neighborhood &amp; Residents Purchasing Alliance — Postcard</title>
<link rel="stylesheet" href="https://fonts.googleapis.com/css2?family=Lora:wght@400;700&display=swap">
<style>
  :root {
    --plum: #7a1f5c;
    --plum-dark: #5b1746;
    --magenta: #b0408a;
    --green-light: #eef5d4;
    --green: #a8cd5c;
    --green-line: #8dc63f;
    --ink: #4a1438;
    --paper: #ffffff;
    --backdrop: #ecebe7;
  }
  * { box-sizing: border-box; margin: 0; padding: 0; }
  html, body { width: 1200px; height: 900px; overflow: hidden; }
  body { background: var(--backdrop); font-family: "Lora", Georgia, serif; color: var(--ink); position: relative; }

  .postcard { position: absolute; background: var(--paper); box-shadow: 0 3px 10px rgba(0,0,0,.18); overflow: hidden; }
  .postcard > svg { position: absolute; inset: 0; }
  .postcard--front { left: 30px; top: 25px; width: 640px; height: 415px; }
  .postcard--back { left: 560px; top: 470px; width: 600px; height: 390px; }

  .brand { position: absolute; display: flex; align-items: center; gap: 8px; }
  .brand__square { width: 46px; height: 46px; background: var(--plum); flex: none; }
  .brand__name { font-size: 13px; font-weight: 700; line-height: 1.15; color: var(--plum); text-transform: uppercase; letter-spacing: .04em; }
  .postcard--front .brand { left: 405px; top: 84px; width: 225px; }
  .postcard--back .brand { left: 418px; top: 298px; width: 178px; }
  .postcard--back .brand__square { width: 40px; height: 40px; }
  .postcard--back .brand__name { font-size: 10px; line-height: 1.15; letter-spacing: .03em; }

  .section-title { position: absolute; display: flex; align-items: center; gap: 6px; font-weight: 700; font-size: 20px; color: var(--plum); text-transform: uppercase; }
  .section-title svg { width: 26px; height: 26px; flex: none; }
  .postcard--front .section-title { left: 12px; top: 210px; }
  .postcard--back .section-title { left: 10px; top: 192px; }

  .section-copy { position: absolute; font-size: 13px; line-height: 16.5px; color: var(--ink); }
  .postcard--front .section-copy { left: 46px; top: 243px; width: 480px; font-size: 12.6px; }
  .postcard--back .section-copy { left: 14px; top: 222px; width: 392px; font-size: 11.4px; line-height: 14px; text-align: justify; hyphens: auto; }

  .contact { position: absolute; left: 160px; top: 364px; width: 320px; text-align: center; color: #fff; font-size: 9px; line-height: 11.5px; }
  .contact__address { font-size: 9.5px; }

  .site-link { position: absolute; left: 0; width: 410px; top: 364px; text-align: center; color: #fff; font-weight: 700; font-size: 13px; text-decoration: none; }

  .stamp-box { position: absolute; left: 498px; top: 12px; width: 88px; height: 86px; border: 1.5px solid #222; }
  .address-line { position: absolute; left: 448px; width: 140px; height: 0; border-top: 1.2px solid #333; }
</style>
</head>
<body>

<article class="postcard postcard--front" aria-label="Postcard front: Who we are">
  <svg viewBox="0 0 640 415" width="640" height="415">
    <defs>
      <linearGradient id="front-photo-tone" x1="0" y1="0" x2="1" y2="1">
        <stop offset="0" stop-color="#e9b46a"/>
        <stop offset=".5" stop-color="#c98a46"/>
        <stop offset="1" stop-color="#6d4a2c"/>
      </linearGradient>
      <linearGradient id="front-band" x1="0" y1="0" x2="1" y2="0">
        <stop offset="0" stop-color="#a8cd5c"/>
        <stop offset=".45" stop-color="#e6f1c6"/>
        <stop offset="1" stop-color="#a8cd5c"/>
      </linearGradient>
    </defs>
    <polygon points="0,0 455,0 318,175 0,175" fill="url(#front-photo-tone)" role="img" aria-label="Photo: hiker with raised arms on a sunlit mountain ridge"/>
    <polygon points="447,0 462,0 326,178 311,178" fill="var(--green-line)"/>
    <polygon points="462,0 476,0 340,178 326,178" fill="var(--plum)"/>
    <polygon points="0,176 452,176 640,352 640,360 0,360" fill="var(--magenta)"/>
    <polygon points="0,182 448,182 636,358 0,358" fill="url(#front-band)"/>
    <polygon points="0,370 125,370 148,356 486,356 512,370 640,370 640,415 0,415" fill="var(--plum)"/>
  </svg>

  <div class="brand">
    <span class="brand__square"></span>
    <span class="brand__name">Neighborhood &amp; Residents Purchasing Alliance</span>
  </div>

  <h2 class="section-title">
    <svg viewBox="0 0 26 26"><circle cx="13" cy="13" r="11.5" fill="none" stroke="var(--plum)" stroke-width="2"/><rect x="7" y="9" width="12" height="8" fill="none" stroke="var(--plum)" stroke-width="1.6"/><line x1="9" y1="12" x2="17" y2="12" stroke="var(--plum)" stroke-width="1.2"/></svg>
    Who We Are
  </h2>
  <p class="section-copy">Comprised of the most talented and progressive companies in North America, NRPA (Neighborhood &amp; Residents Purchasing Alliance) aims to help members seize opportunities and improve profitability. We are a select group of independently owned Homeowner Associations and Management Companies focused on securing our futures, increasing our competitiveness, and offering our clients an unforgettable experience.</p>

  <div class="contact">
    <p class="contact__address">412 Harbor Mill Road Concord, NH 03301</p>
    <p>Dana Whitlock, PCAM President</p>
    <p>555.014.2290</p>
    <p>www.joinvelarta.com</p>
  </div>
</article>

<article class="postcard postcard--back" aria-label="Postcard back: What we do">
  <svg viewBox="0 0 600 390" width="600" height="390">
    <defs>
      <linearGradient id="back-photo-tone" x1="0" y1="0" x2="1" y2="0">
        <stop offset="0" stop-color="#8a8f86"/>
        <stop offset=".5" stop-color="#b9c99a"/>
        <stop offset="1" stop-color="#5f7696"/>
      </linearGradient>
      <linearGradient id="back-panel" x1="0" y1="0" x2="1" y2="0">
        <stop offset="0" stop-color="#a8cd5c"/>
        <stop offset=".5" stop-color="#e6f1c6"/>
        <stop offset="1" stop-color="#a8cd5c"/>
      </linearGradient>
    </defs>
    <rect x="0" y="0" width="410" height="365" fill="url(#back-panel)"/>
    <polygon points="0,0 395,0 260,185 0,185" fill="url(#back-photo-tone)" role="img" aria-label="Photo: two men looking down together at a shared document outdoors"/>
    <polygon points="395,0 408,0 272,188 259,188" fill="var(--plum)"/>
    <polygon points="0,185 260,185 256,191 0,191" fill="var(--plum)"/>
    <rect x="0" y="355" width="600" height="35" fill="var(--plum)"/>
  </svg>

  <div class="stamp-box" aria-hidden="true"></div>
  <span class="address-line" style="top:148px"></span>
  <span class="address-line" style="top:183px"></span>
  <span class="address-line" style="top:220px"></span>

  <h2 class="section-title">
    <svg viewBox="0 0 26 26"><circle cx="13" cy="13" r="11.5" fill="none" stroke="var(--plum)" stroke-width="2"/><circle cx="13" cy="13" r="6" fill="none" stroke="var(--plum)" stroke-width="1.6"/><line x1="13" y1="9" x2="13" y2="17" stroke="var(--plum)" stroke-width="1.4"/></svg>
    What We Do
  </h2>
  <p class="section-copy" lang="en">NRPA was created to bring the power of scale to companies and communities like yours. Our alliance works to enhance the value of all members through peer-to-peer networking, savings on products and services, and support for the entrepreneurial spirit. By joining forces with other likeminded members you are able to gain access to our PooledReach platform that leverages our memberships collective strength to offer programs and services independent companies and communities likely can't achieve on their own.</p>

  <div class="brand">
    <span class="brand__square"></span>
    <span class="brand__name">Neighborhood &amp; Residents Purchasing Alliance</span>
  </div>

  <a class="site-link" href="http://joinvelarta.com">www.joinvelarta.com</a>
</article>

</body>
</html>
```